Vermilion Reel Works Web Design

COMPANY: VERMILION REEL WORKS
LOCATION: SHANGHAI, CHINA
AREA: FILM/TV DRAMA/COMMERCIALS/GAME POST PRODUCTION, SOUND DESIGN, MUSIC, and GAME.
WEB STYLE: SIMPLE, PROFESSIONAL, TRUSTWORTHY

LANGUAGE: ENGLISH, CHINESE. (Same layout, different language)
UPDATE: AFTER PROJECT FINISHED, WE NEED UPDATE BY OURSELVES.

MAIN SUBJECT: 6
1 HOMEPAGE
2 ABOUT US
3 TEAM
4 SERVICES
5 FACILITY
6 CONTACT

add one page of JOB OPPORTUNITIES.

DETAILS
1 HOMEPAGE
SLOGAN: Vermilion Reel Works provides a well-designed working environment which amplifies your team’s ability to reach their creative goals.

Our services include:
 Feature Films
 Music & Scoring
 Commercials
 ADR & Foley
 Sound & Picture Editorial
 Sound Design
 Video Game

2 ABOUT US
Vermilion Reel Works is located in the premiere South-Bund area of Shanghai. Occupying a 5000 square meter Technical Building, Vermilion Reel Works was built by a filmmaker for filmmakers, and is one of the largest, most versatile full-service post-production facilities in China.

Vermilion Reel Works is positioning to be at the forefront of the latest technology. Our goal is to provide a comprehensive solution for the post-production needs of our clients. We offer two fully-equipped dubbing stages (one of which will be certified KESTRON VOXAR PREMIERE), a large variety of both picture and sound editing rooms, impressive Foley and ADR stages, a world-class scoring stage, and complete audio and video transfer services.

We can handle your entire project from editing all the way to the end of the final sound mix; all under one extremely comfortable roof. We fully realize that the true art is in listening to the needs of our clients and making their greatest vision a reality. To this end our creative team's expertise, with a network of sound supervisors, editors and mixers, will deliver the magic you need. Producers and directors will also find our richly appointed guest accommodations to be a comfortable and soothing place to wind up the day. Every aspect of your project will be taken care of by a skilled and dedicated team, in the way that is best suited to you.

3 TEAM
(attachment 01)

4 SERVICES
Sound Mix
ADR
FOLEY
MUSIC
Sound Design
Sound Edit
Picture Edit
for all the Films, TV Drama, Commercials, Video Games, Online Media
(attachment 02, use photo)

5 FACILITY
(attachment 03)

6 CONTACT
(attachment04)
with map

Project Deadline Extended
Reason: Designers work are great, my bosses will spend 1-2 days select one of these web design, and spend 1-2 days to make some change, maybe use new photos.

```html
<!DOCTYPE html>
<html lang="en">
<head>
<meta charset="utf-8">
<title>Vermilion Reel Works</title>
<link href="https://fonts.googleapis.com/css2?family=Lato:wght@300;400;700&family=Playfair+Display:wght@400;700&display=swap" rel="stylesheet">
<style>
:root{
  --teal:#2ad3b0;
  --teal-line:#27c9a6;
  --red:#e2474b;
  --ink:#2b2b2b;
  --muted:#6a6a6a;
  --rule:#e6e6e6;
  --blog-bg:#2b2b2b;
  --foot-bg:#333435;
  --foot-text:#8c8c8c;
  --white:#ffffff;
}
*{margin:0;padding:0;box-sizing:border-box}
html,body{width:704px;height:1200px;overflow:hidden}
body{position:relative;font-family:'Lato',sans-serif;color:var(--ink);background:var(--white)}
.abs{position:absolute}
.serif{font-family:'Playfair Display',serif}

/* hero */
.hero{left:0;top:0;width:704px;height:290px;overflow:hidden}
.hero-photo{position:absolute;inset:0;background:
  radial-gradient(ellipse at 20% 85%,rgba(160,170,40,.35),transparent 40%),
  radial-gradient(ellipse at 80% 20%,rgba(60,90,140,.35),transparent 45%),
  linear-gradient(160deg,#3b4a4f 0%,#1c2428 45%,#2d3a3c 70%,#151b1d 100%)}
.brand{left:100px;top:10px;color:var(--white);font-family:'Playfair Display',serif;font-size:13px;line-height:12px;text-align:center;font-weight:400}
.brand small{display:block;font-size:8px;line-height:10px}
.nav{top:22px;left:292px;display:flex;gap:0;color:var(--white);font-size:8px}
.nav a{color:inherit;text-decoration:none;position:absolute;white-space:nowrap}
.nav a.active::after{content:"";position:absolute;left:0;right:0;top:13px;height:2px;background:var(--teal)}
.lang{left:595px;top:5px;width:15px;height:15px;border-radius:50%;background:var(--red);color:var(--white);font-size:6px;line-height:15px;text-align:center}
.hero-title{left:0;width:704px;top:134px;text-align:center;color:var(--white);font-weight:700;font-size:21px}
.hero-tag{left:0;width:704px;top:158px;text-align:center;color:var(--white);font-family:'Playfair Display',serif;font-size:13.5px;line-height:18px}

/* section headings */
.heading{text-align:center;font-family:'Playfair Display',serif;font-size:11px}
.heading::after{content:"";display:block;width:38px;height:2px;margin:5px auto 0;background:var(--teal)}

/* services */
.service{width:132px;text-align:center}
.service h3{font-family:'Playfair Display',serif;font-weight:400;font-size:9.5px;line-height:11px;margin-bottom:7px}
.service p{font-size:6.3px;line-height:9.5px;color:var(--muted);padding:0 10px}
.vrule{width:1px;background:var(--rule)}
.hrule{height:1px;background:var(--rule)}

/* studio band */
.studio{left:0;top:640px;width:704px;height:248px;background:var(--teal);color:var(--white)}
.studio .heading{color:var(--white)}
.studio .heading::after{background:var(--white)}
.create{position:absolute;left:96px;width:250px;text-align:center}
.btn{position:absolute;left:176px;top:204px;width:88px;height:21px;border:1.5px solid var(--white);font-size:6px;font-weight:700;line-height:18px;text-align:center}
.video{left:359px;top:53px;width:250px;height:145px;background:linear-gradient(135deg,#7a6a4a 0%,#4a4434 40%,#2a2a2a 70%,#6a5a3a 100%)}

/* blog */
.blog{left:0;top:888px;width:704px;height:189px;background:var(--blog-bg);color:var(--white)}
.blog .heading{color:var(--white)}
.blog .heading::after{background:var(--white)}
.post{position:absolute;top:52px;width:119px}
.post .thumb{height:81px}
.post time{display:block;margin-top:7px;font-size:5px;color:#9a9a9a;letter-spacing:.2px}
.post h4{font-size:8.5px;line-height:10px;font-weight:700;margin-top:3px}
.arrow{position:absolute;top:84px;width:18px;height:18px;border:1px solid #555;border-radius:50%}

/* footer */
.footer{left:0;top:1077px;width:704px;height:123px;background:var(--foot-bg);color:var(--foot-text)}
.f-icon{position:absolute;top:22px;width:30px;height:30px;border-radius:50%;background:#5c9fd0;border:3px solid #d8e6ef}
.f-text{position:absolute;top:25px;font-size:6.8px;line-height:10px}
.social{position:absolute;top:64px;width:19px;height:19px;border-radius:4px}
.copy{position:absolute;top:92px;left:0;width:704px;text-align:center;font-size:6.5px}
</style>
</head>
<body>

<header class="abs hero">
  <div class="hero-photo" role="img" aria-label="Close-up photo of a mixing console with rows of knobs and faders"></div>
  <div class="abs brand">VERMILION<small>REEL WORKS</small></div>
  <nav class="abs nav" style="left:0;top:22px;width:704px">
    <a class="active" style="left:292px">Home</a>
    <a style="left:330px">About Us</a>
    <a style="left:379px">Team</a>
    <a style="left:414px">Services</a>
    <a style="left:460px">Facility</a>
    <a style="left:502px">Job Opportunities</a>
    <a style="left:582px">Contact</a>
  </nav>
  <div class="abs lang">EN</div>
  <svg class="abs" style="left:341px;top:99px" width="22" height="16" viewBox="0 0 22 16" aria-hidden="true">
    <g fill="var(--red)"><rect x="1" y="4" width="3" height="12"/><rect x="5" y="8" width="3" height="8"/><rect x="9" y="2" width="3" height="14"/><rect x="13" y="7" width="3" height="9"/><rect x="17" y="10" width="3" height="6"/></g>
  </svg>
  <h1 class="abs hero-title">Vermilion Reel Works</h1>
  <p class="abs hero-tag">provides a well-designed working environment which amplifies your team's<br>ability to reach their creative goals.</p>
  <svg class="abs" style="left:341px;top:212px" width="22" height="16" viewBox="0 0 22 16" aria-hidden="true">
    <g fill="var(--red)"><rect x="1" y="4" width="3" height="12"/><rect x="5" y="8" width="3" height="8"/><rect x="9" y="2" width="3" height="14"/><rect x="13" y="7" width="3" height="9"/><rect x="17" y="10" width="3" height="6"/></g>
  </svg>
</header>

<section>
  <h2 class="abs heading" style="left:0;width:704px;top:309px;font-weight:400">Our Service</h2>

  <div class="abs vrule" style="left:220px;top:345px;height:133px"></div>
  <div class="abs vrule" style="left:352px;top:345px;height:133px"></div>
  <div class="abs vrule" style="left:484px;top:345px;height:133px"></div>
  <div class="abs hrule" style="left:95px;top:478px;width:515px"></div>
  <div class="abs vrule" style="left:286px;top:478px;height:132px"></div>
  <div class="abs vrule" style="left:418px;top:478px;height:132px"></div>

  <!-- row one -->
  <div class="abs service" style="left:88px;top:349px">
    <svg width="28" height="28" viewBox="0 0 28 28" aria-hidden="true"><rect x="4" y="2" width="20" height="24" fill="#555"/><g fill="#ddd"><rect x="5.5" y="4" width="3" height="3"/><rect x="5.5" y="10" width="3" height="3"/><rect x="5.5" y="16" width="3" height="3"/><rect x="5.5" y="22" width="3" height="3"/><rect x="19.5" y="4" width="3" height="3"/><rect x="19.5" y="10" width="3" height="3"/><rect x="19.5" y="16" width="3" height="3"/><rect x="19.5" y="22" width="3" height="3"/></g><rect x="10" y="4" width="8" height="9" fill="#888"/><rect x="10" y="15" width="8" height="9" fill="#888"/></svg>
    <h3 style="margin-top:12px">Feature Films</h3>
    <p>Sed ut perspiciatis unde omnis iste natus error sit voluptatem accusantium doloremque laudantium,</p>
  </div>
  <div class="abs service" style="left:220px;top:349px">
    <svg width="28" height="28" viewBox="0 0 28 28" aria-hidden="true"><rect x="2" y="1" width="7" height="26" rx="3.5" fill="#333"/><rect x="10.5" y="1" width="7" height="26" rx="3.5" fill="#2ad3b0"/><rect x="19" y="1" width="7" height="26" rx="3.5" fill="#9b7fd6"/><circle cx="5.5" cy="9" r="3" fill="#f2a93b"/><circle cx="14" cy="18" r="3" fill="#e2474b"/><circle cx="22.5" cy="11" r="3" fill="#fff"/></svg>
    <h3 style="margin-top:12px">Music &amp; Scoring</h3>
    <p>Sed ut perspiciatis unde omnis iste natus error sit voluptatem accusantium doloremque laudantium,</p>
  </div>
  <div class="abs service" style="left:352px;top:349px">
    <svg width="30" height="28" viewBox="0 0 30 28" aria-hidden="true"><rect x="1" y="2" width="28" height="23" rx="2" fill="#3a4a5c"/><rect x="4" y="5" width="22" height="13" fill="#f3d79a"/><rect x="6" y="20" width="18" height="2" fill="#8aa"/></svg>
    <h3 style="margin-top:12px">Commercials</h3>
    <p>Sed ut perspiciatis unde omnis iste natus error sit voluptatem accusantium doloremque laudantium,</p>
  </div>
  <div class="abs service" style="left:484px;top:349px">
    <svg width="28" height="30" viewBox="0 0 28 30" aria-hidden="true"><rect x="8" y="1" width="12" height="18" rx="6" fill="#2aa6a6"/><path d="M5 13a9 9 0 0 0 18 0" fill="none" stroke="#3a4a5c" stroke-width="2"/><rect x="13" y="22" width="2" height="5" fill="#3a4a5c"/><rect x="8" y="27" width="12" height="2" fill="#3a4a5c"/></svg>
    <h3 style="margin-top:10px">ADR &amp; Foley</h3>
    <p>Sed ut perspiciatis unde omnis iste natus error sit voluptatem accusantium doloremque laudantium,</p>
  </div>

  <!-- row two -->
  <div class="abs service" style="left:154px;top:502px">
    <svg width="30" height="28" viewBox="0 0 30 28" aria-hidden="true"><rect x="2" y="3" width="20" height="18" fill="#f0c48a" transform="rotate(-8 12 12)"/><rect x="5" y="6" width="14" height="11" fill="#5aa0c8" transform="rotate(-8 12 12)"/><circle cx="22" cy="22" r="4" fill="#e07a3a"/><rect x="25" y="10" width="1.8" height="12" fill="#e07a3a"/></svg>
    <h3 style="margin-top:12px">Sound &amp; Picture<br>Editorial</h3>
    <p>Sed ut perspiciatis unde omnis iste natus error sit voluptatem accusantium doloremque laudantium,</p>
  </div>
  <div class="abs service" style="left:286px;top:502px">
    <svg width="30" height="26" viewBox="0 0 30 26" aria-hidden="true"><g><rect x="1" y="20" width="28" height="4" fill="#e2474b"/><rect x="1" y="14" width="28" height="4" fill="#f08a4b"/><rect x="5" y="8" width="20" height="4" fill="#f2c14b"/><rect x="11" y="2" width="8" height="4" fill="#5fc4b0"/></g></svg>
    <h3 style="margin-top:12px">Sound Design</h3>
    <p>Sed ut perspiciatis unde omnis iste natus error sit voluptatem accusantium doloremque laudantium,</p>
  </div>
  <div class="abs service" style="left:418px;top:502px">
    <svg width="28" height="28" viewBox="0 0 28 28" aria-hidden="true"><rect x="13" y="1" width="2" height="5" fill="#3a4a5c"/><circle cx="14" cy="2" r="2" fill="#3a4a5c"/><rect x="3" y="6" width="22" height="20" rx="3" fill="#4a78c0"/><circle cx="9.5" cy="14" r="3" fill="#fff"/><circle cx="18.5" cy="14" r="3" fill="#fff"/><rect x="9" y="20" width="10" height="2" fill="#fff"/></svg>
    <h3 style="margin-top:12px">Video Game</h3>
    <p>Sed ut perspiciatis unde omnis iste natus error sit voluptatem accusantium doloremque laudantium,</p>
  </div>
</section>

<section class="abs studio">
  <h2 class="abs heading" style="left:120px;width:200px;top:20px;font-weight:700">Work With Our Studio</h2>
  <div class="create" style="top:61px">
    <p style="font-weight:700;font-size:14.5px;line-height:16px">WE CREATE</p>
    <p class="serif" style="font-size:22px;line-height:26px">Digital Experience</p>
    <p style="font-weight:300;font-size:18px;line-height:22px">for modern</p>
    <p style="font-weight:300;font-size:18px;line-height:22px">digital world companies</p>
    <p style="font-size:6.5px;line-height:9px;margin-top:7px">Lorem ipsum dolor sit amet, consectetur adipisicing elit, sed do eiusmod tempor incididunt ut labore et dolore magna aliqua.</p>
  </div>
  <div class="btn">FIND OUT HOW</div>

  <h2 class="abs heading" style="left:359px;width:250px;top:20px;font-weight:700">Vermilion Reel Works Case Study</h2>
  <div class="abs video" role="img" aria-label="Video still of an engineer working at a mixing desk in a post-production suite"></div>
  <svg class="abs" style="left:466px;top:106px" width="36" height="36" viewBox="0 0 36 36" aria-hidden="true"><circle cx="18" cy="18" r="17" fill="rgba(0,0,0,.55)" stroke="#fff" stroke-width="1.5"/><path d="M14 11l12 7-12 7z" fill="#fff"/></svg>
  <p class="abs" style="left:359px;top:210px;width:250px;font-size:6.5px;line-height:9px;font-weight:700">Lorem ipsum dolor sit amet, consectetur adipisicing elit, sed do eiusmod tempor incididunt ut labore et dolore magna aliqua.</p>
</section>

<section class="abs blog">
  <h2 class="abs heading" style="left:0;width:704px;top:20px;font-weight:700">From The Blog</h2>
  <div class="arrow" style="left:123px"><svg width="16" height="16" viewBox="0 0 16 16" aria-hidden="true"><path d="M9.5 4.5L6 8l3.5 3.5" fill="none" stroke="#666" stroke-width="1.2"/></svg></div>
  <div class="arrow" style="left:563px"><svg width="16" height="16" viewBox="0 0 16 16" aria-hidden="true"><path d="M6.5 4.5L10 8l-3.5 3.5" fill="none" stroke="#666" stroke-width="1.2"/></svg></div>
  <article class="post" style="left:174px">
    <div class="thumb" role="img" aria-label="Photo of a rack-mounted audio unit with a perforated front panel" style="background:linear-gradient(180deg,#2a2a2a 0%,#b8ad96 35%,#8e846f 70%,#3a352c 100%)"></div>
    <time>FEBRUARY 3, 2014</time>
    <h4>Donec ultricies nunc id rutrum consectetur.</h4>
  </article>
  <article class="post" style="left:293px">
    <div class="thumb" role="img" aria-label="Photo of a studio rack with coloured indicator buttons and knobs" style="background:linear-gradient(135deg,#5a4a2a 0%,#2a2418 40%,#6a5020 70%,#1a1612 100%)"></div>
    <time>FEBRUARY 3, 2014</time>
    <h4>Donec ultricies nunc id rutrum consectetur.</h4>
  </article>
  <article class="post" style="left:412px">
    <div class="thumb" role="img" aria-label="Photo of a compact mixing surface on a studio desk" style="background:linear-gradient(135deg,#a08050 0%,#6a5436 45%,#3a3026 75%,#c8b89a 100%)"></div>
    <time>FEBRUARY 3, 2014</time>
    <h4>Donec ultricies nunc id rutrum consectetur.</h4>
  </article>
</section>

<footer class="abs footer">
  <div class="f-icon" style="left:96px;background:#6a8fb8"><svg width="24" height="24" viewBox="0 0 24 24" aria-hidden="true"><circle cx="12" cy="12" r="6" fill="none" stroke="#fff" stroke-width="2"/><circle cx="12" cy="12" r="2" fill="#fff"/></svg></div>
  <p class="f-text" style="left:139px">中国上海黄浦区澄岸路58号<br>No.58 Chengan Rd.<br>Shanghai China, 200011</p>
  <div class="f-icon" style="left:271px"><svg width="24" height="24" viewBox="0 0 24 24" aria-hidden="true"><path d="M8 5c1 0 2 3 2 4s-1.5 1.5-1 2.5 2.5 3.5 3.5 4 1.5-1 2.5-1 4 1 4 2-1.5 2.5-3 2.5C10 19 5 14 5 8c0-1.5 2-3 3-3z" fill="#fff"/></svg></div>
  <p class="f-text" style="left:314px">86 21 5550-0142<br>400-555-0188 (REEL)</p>
  <div class="f-icon" style="left:447px"><svg width="24" height="24" viewBox="0 0 24 24" aria-hidden="true"><rect x="5" y="7" width="14" height="10" fill="#fff"/><path d="M5 7l7 6 7-6" fill="none" stroke="#5c9fd0" stroke-width="1.2"/></svg></div>
  <p class="f-text" style="left:490px">hello@vermilionreel.example</p>
  <span class="social" style="left:305px;background:#4aa8e0"></span>
  <span class="social" style="left:330px;background:#3b5a9a"></span>
  <span class="social" style="left:355px;background:#1a7ab5"></span>
  <span class="social" style="left:380px;background:#d9473a"></span>
  <p class="copy">© 2014 Vermilion Reel Works</p>
</footer>

</body>
</html>
```